BrivoLane Ute.

I want the full logo on one side. And the other side the card if right Ralf the logo the left half orange like the car in the logo color with Danielle R Morrow
Founder and CEO
Email symbol then dmorrow@brivolaneute.com
Www symbol. Then Brivolaneute.com
Phone symbol then 413-926-BRIV
The very bottom would like Brivo Lane Ute is a division of Harmond Vistas. LLC

```html
<!DOCTYPE html>
<html lang="en">
<head>
<meta charset="utf-8">
<title>Brivo Lane Ute — Business Card</title>
<link href="https://fonts.googleapis.com/css2?family=Lato:wght@400;700&display=swap" rel="stylesheet">
<style>
  :root {
    --backdrop: #e7e4e1;
    --card: #ffffff;
    --band: #fbdcc2;
    --orange: #f0952a;
    --ink: #2b2522;
    --rule: #8c817a;
    --red: #e8473b;
  }
  * { box-sizing: border-box; margin: 0; padding: 0; }
  html, body {
    width: 1200px; height: 844px; overflow: hidden;
    background: var(--backdrop);
    font-family: "Lato", Arial, sans-serif;
  }
  .stage {
    position: relative; width: 1200px; height: 844px;
    display: flex; align-items: center; justify-content: center; gap: 60px;
  }
  .card {
    position: relative; width: 520px; height: 300px;
    background: var(--card);
    box-shadow: 0 6px 18px rgba(0,0,0,.18);
    overflow: hidden;
  }
  /* front */
  .card-front .band {
    position: absolute; left: 0; right: 0; top: 82px; height: 188px;
    background: var(--band);
  }
  .brand-mini {
    position: absolute; top: 40px; left: 0; right: 0;
    display: flex; align-items: center; justify-content: center; gap: 8px;
    font-weight: 700; font-size: 20px; color: var(--orange);
  }
  .brand-dot { width: 14px; height: 14px; border-radius: 50%; background: var(--orange); }
  .contact {
    position: absolute; top: 98px; left: 0; right: 0;
    text-align: center; color: var(--ink);
  }
  .contact .name {
    font-weight: 700; font-size: 19px; color: var(--orange);
    text-transform: uppercase; letter-spacing: .3px;
  }
  .contact .role { font-size: 14px; margin-top: 1px; }
  .icon-row {
    display: flex; align-items: center; justify-content: center; gap: 5px;
    margin: 8px auto 6px;
  }
  .icon-row .rule { width: 72px; height: 1px; background: var(--rule); }
  .icon-row svg { width: 18px; height: 18px; display: block; }
  .contact .line { font-size: 15px; line-height: 21px; }
  /* back */
  .card-back {
    display: flex; flex-direction: column; align-items: center; justify-content: center;
  }
  .brand-lockup {
    display: flex; align-items: center; gap: 12px;
    font-weight: 700; font-size: 36px; color: var(--ink);
    text-transform: uppercase; letter-spacing: 1px;
    margin-top: -30px;
  }
  .brand-lockup .brand-dot { width: 26px; height: 26px; }
  .division {
    position: absolute; bottom: 62px; left: 0; right: 0; text-align: center;
    font-size: 13.5px; color: var(--red); text-transform: uppercase; letter-spacing: .2px;
  }
</style>
</head>
<body>
<main class="stage">
  <section class="card card-front" aria-label="Card front">
    <div class="band"></div>
    <div class="brand-mini"><span class="brand-dot"></span>Brivo Lane Ute</div>
    <div class="contact">
      <p class="name">Danielle R Morrow</p>
      <p class="role">Founder and CEO</p>
      <div class="icon-row">
        <span class="rule"></span>
        <svg viewBox="0 0 20 20" aria-label="Phone"><circle cx="10" cy="10" r="10" fill="var(--orange)"/><path d="M6.5 5.5l2 0 1 2.5-1.3 1a6 6 0 0 0 2.8 2.8l1-1.3 2.5 1v2a1 1 0 0 1-1 1A8 8 0 0 1 5.5 6.5a1 1 0 0 1 1-1z" fill="#fff"/></svg>
        <svg viewBox="0 0 20 20" aria-label="Email"><circle cx="10" cy="10" r="10" fill="var(--orange)"/><rect x="5" y="6.5" width="10" height="7" fill="#fff"/><path d="M5 6.5l5 4 5-4" fill="none" stroke="var(--orange)" stroke-width="1"/></svg>
        <svg viewBox="0 0 20 20" aria-label="Website"><circle cx="10" cy="10" r="10" fill="var(--orange)"/><g fill="none" stroke="#fff" stroke-width="1.2"><circle cx="10" cy="10" r="5"/><ellipse cx="10" cy="10" rx="2.2" ry="5"/><path d="M5 10h10"/></g></svg>
        <span class="rule"></span>
      </div>
      <p class="line">413-926-BRIV</p>
      <p class="line">dmorrow@brivolaneute.com</p>
      <p class="line">www.brivolaneute.com</p>
    </div>
  </section>

  <section class="card card-back" aria-label="Card back">
    <div class="brand-lockup"><span class="brand-dot"></span>Brivo Lane Ute</div>
    <p class="division">Brivo Lane Ute is a division of Harmond Vistas. LLC</p>
  </section>
</main>
</body>
</html>
```